Design signage & window art that screams: “This is the place for wall decor!”

Contest Goal:
Design a single, cohesive storefront signage system for Ontario Decor. That includes the top fascia and bottom window graphics, presented as one polished connected visual package. Designers will provide a composite mock-up showing how the overall design looks in context.

***All Designs need to creatively incorporate the torn paper effect where the showroom is located .Example found attached(Window-Graphics_Inspo.jpg)

Category taglines
Each product section (at the bottom of each window group) should include bold, eye-catching taglines. Use the examples below — final wording may be refined later.
Window image focus clarified
Left side: Product closeups and detail shots
Right side: Lifestyle/in-room imagery

2. Layout Specifications/Dimensions
Fascia: 148 ft wide × 4 ft high
Regular windows: approx. 49” × 36”
Door glass: approx. 75” × 30”
Yellow zone (NewStorefrnt.png): Showroom windows + doors — must preserve visibility
Blue zones: All windows eligible for full-coverage graphics
Assets:

3. Fascia Signage (Top Strip)
Background: Solid black or deep charcoal
Font: Bold, modern, highly legible Silver/white is preferred.
Left-aligned text layout (in this order):
Wallpaper
Murals
Panels
VantaWallHouse.com
Brelwick Interiors (just the logo,it must be the same size as other top font)
Note: Do not include any taglines with the Brelwick Interiors logo — the product categories are already clearly spelled out.

4. Window Graphics (Lower Section)
Design a seamless visual layout across the storefront windows that reflects each product category. Each window section must line up directly below its corresponding fascia label.
Section Breakdown:
Wallpaper
Visuals: Close-up patterns, roll textures, product shots
Tagline: Don’t Paint Over Potential. Wallpaper It.
Murals
Visuals: Large-scale mural applications, dramatic visuals
Tagline: Mural of the Story? Your Walls Matter.
Panels
Visuals: Slat walls, acoustic panels, product installations
Tagline: Slat Happens. We got you covered!

5. Showroom Zone (Yellow Area in Layout)
Apply the torn-paper effect from Window-Graphics_Inspo.jpg within the yellow showroom area
This should simulate a dramatic peel-back revealing the showroom interior while maintaining clear visibility and fitting seamlessly with the surrounding design.

6. Visual Structure Guide
Left windows: Product closeups and material textures
Right windows: Styled room scenes and optional torn-paper aesthetic (some torn effect could be used on the left side too, if it works compositionally)
Taglines: Must be visually emphasized in each section
Overall layout should be clean, balanced, and contemporary

7. Final Goals
Maintain alignment between fascia text and window content
Keep the entrance clean and unobstructed
Communicate Brelwick Interiors’s brand clearly: modern, bold, and functional

Target Market(s)

Homeowners, interior designers, contractors, and DIY renovators looking for premium wall decor solutions such as wallpaper, decorative panels, and murals. Most customers are style-conscious, value design, and want to enhance living or commercial spaces with bold, modern decor elements.

Industry/Entity Type

Interior Design / Home Improvement / Retail

Requirements
Must have
• • A single cohesive design that integrates both the top signage and window graphics • The text: “Vantawallhouse.com | Panels | Wallpaper | Murals” plus the Brelwick Interiors logo • High legibility from a distance (ideal for street traffic) • A clear, well-lit showroom entrance (yellow-marked section must stay mostly transparent) •The torn paper effect(Window-Graphics_Inspo.jpg) • Visual alignment between fascia and windows (should feel like one system)
Nice to have
• Use of subtle framing, transparency, or frosted effects to blend the entrance into the full design • Modern typography and layout styles • Elements inspired by included reference files (especially “BottomIdeaInspo” and “Window-Graphics”) • Visual references to wallpaper, panels, or mural-style art in the window graphics • A few creative layout options or variations of the final concept (if time allows)
Should not have
• Should not haves • Cluttered or overly busy designs • Serif or ornate fonts that are hard to read at a distance • Fully opaque designs on the showroom entrance • Literal or outdated imagery(provided in WallpaperMuralAndPanelImages.zip they are supposed to help guide your design,Please dont only use those as the images) — the overall tone should be bold and modern, not traditional

```html
<!DOCTYPE html>
<html lang="en">
<head>
<meta charset="utf-8">
<title>Brelwick Interiors – Storefront Elevations CC / DD</title>
<link rel="stylesheet" href="https://fonts.googleapis.com/css2?family=Roboto+Condensed:wght@300;400;700&family=Fira+Sans+Condensed:wght@400;600;700&family=Arimo&display=swap">
<style>
  :root{
    --paper:#ffffff;
    --sheet-edge:#dcdcdc;
    --mullion:#7d7d7d;
    --fascia:#231f20;
    --fascia-glow:#3a3536;
    --fascia-ink:#ffffff;
    --frame-red:#d7261e;
    --label-red:#d7261e;
    --showroom-glass:#fbf5a2;
    --torn-edge:#fdfcf6;
    --torn-shadow:rgba(60,50,30,.35);
    --swoosh:#6cb33f;
    --ink-blue:#0d4a8f;
    --ink-red:#d7261e;
    --ink-purple:#8b1a7f;
  }
  *{box-sizing:border-box;margin:0;padding:0}
  html,body{width:1200px;height:847px;overflow:hidden;background:var(--paper)}
  .sheet{position:relative;width:1200px;height:847px;border:1px solid var(--sheet-edge);background:var(--paper)}
  .svg-defs{position:absolute;width:0;height:0}

  .elevation{position:absolute;left:0;width:1200px;height:160px}
  .elevation--cc{top:193px}
  .elevation--dd{top:493px}

  .elevation__label{position:absolute;left:44px;top:58px;font-family:"Arimo",sans-serif;font-size:19px;color:var(--label-red)}

  .transom{position:absolute;top:0;height:53px;border-right:1px solid var(--mullion);border-bottom:1px solid var(--mullion);
    background-image:linear-gradient(to right,var(--mullion) 1px,transparent 1px),linear-gradient(to bottom,var(--mullion) 1px,transparent 1px);
    background-size:calc(100% / var(--cols)) 50%;}

  .fascia{position:absolute;left:97px;top:52px;width:1057px;height:41px;
    background:radial-gradient(ellipse at 30% 50%,var(--fascia-glow),var(--fascia) 60%);color:var(--fascia-ink)}
  .fascia__item{position:absolute;top:50%;transform:translate(-50%,-50%);white-space:nowrap;font-family:"Roboto Condensed",sans-serif}
  .fascia__category{font-weight:700;font-size:25px;letter-spacing:1.5px}
  .fascia__web{font-weight:300;font-size:16px;letter-spacing:3.2px}
  .fascia__phone{font-weight:400;font-size:17px;letter-spacing:.6px}
  .fascia__brand{font-weight:400;font-size:16px;letter-spacing:.6px;text-transform:uppercase}

  .window{position:absolute;top:93px;height:67px;border:1px solid var(--frame-red);background:var(--paper);overflow:hidden}
  .window__header{height:21px;display:flex;align-items:center;justify-content:center;gap:3px;white-space:nowrap;font-family:"Fira Sans Condensed",sans-serif}
  .tagline__lead{font-size:5.5px;font-weight:600}
  .tagline__main{font-size:9.5px;font-weight:700}
  .tagline--blue{color:var(--ink-blue)}
  .tagline--red{color:var(--ink-red)}
  .tagline--purple{color:var(--ink-purple)}
  .window__placeholder{font-size:9.5px;font-weight:700;letter-spacing:-.2px}
  .window__placeholder--light{font-weight:400;color:var(--ink-blue)}
  .window__art{position:absolute;left:0;right:0;bottom:0;height:44px}
  .window__art svg{display:block;width:100%;height:100%}
  .window__overlay{position:absolute;right:3px;bottom:3px;text-align:center;color:#fff;font-family:"Fira Sans Condensed",sans-serif;line-height:1.05}
  .window__overlay .tagline__lead{display:block}
  .window__overlay .tagline__main{display:block}

  .showroom{position:absolute;left:534px;top:93px;width:284px;height:67px}
  .showroom__glass{position:absolute;top:0;height:67px;background-color:var(--showroom-glass);
    border-right:1px solid var(--frame-red);
    background-image:linear-gradient(to right,var(--frame-red) 1px,transparent 1px),linear-gradient(to bottom,var(--frame-red) 1px,transparent 1px);
    background-size:calc(100% / var(--cols)) 22px}
  .showroom__glass--left{left:0;width:91px;--cols:3}
  .showroom__glass--right{left:145px;width:139px;--cols:4}
  .showroom__tear{position:absolute;left:0;top:0;width:284px;height:67px;pointer-events:none}
  .entrance{position:absolute;left:91px;top:0;width:54px;height:67px;background:var(--showroom-glass)}
  .entrance__frame{position:absolute;left:5px;top:15px;width:44px;height:49px;border:1px solid var(--frame-red);display:flex;gap:2px;padding:2px}
  .entrance__leaf{flex:1;display:flex;flex-direction:column;gap:2px}
  .entrance__pane{flex:1;border:1px solid var(--frame-red)}
</style>
</head>
<body>
<main class="sheet">

  <svg class="svg-defs" aria-hidden="true">
    <defs>
      <linearGradient id="tear-band" x1="0" y1="0" x2="1" y2="0">
        <stop offset="0" stop-color="#6d6550"/>
        <stop offset=".5" stop-color="#8a7c5c"/>
        <stop offset="1" stop-color="#6d6550"/>
      </linearGradient>
      <linearGradient id="tear-flap" x1="0" y1="0" x2="1" y2="1">
        <stop offset="0" stop-color="#fdfcf6"/>
        <stop offset="1" stop-color="#cfc6a8"/>
      </linearGradient>
    </defs>
  </svg>

  <!-- Elevation CC -->
  <section class="elevation elevation--cc">
    <span class="elevation__label">-CC-</span>

    <div class="transom" style="left:97px;width:139px;--cols:4"></div>
    <div class="transom" style="left:242px;width:140px;--cols:4"></div>
    <div class="transom" style="left:388px;width:139px;--cols:4"></div>
    <div class="transom" style="left:534px;width:139px;--cols:4"></div>
    <div class="transom" style="left:679px;width:139px;--cols:4"></div>
    <div class="transom" style="left:825px;width:139px;--cols:4"></div>
    <div class="transom" style="left:972px;width:105px;--cols:3"></div>
    <div class="transom" style="left:1083px;width:71px;--cols:2"></div>

    <div class="fascia">
      <span class="fascia__item fascia__category" style="left:70px">WALLPAPER</span>
      <span class="fascia__item fascia__category" style="left:215px">MURALS</span>
      <span class="fascia__item fascia__category" style="left:361px">PANELS</span>
      <span class="fascia__item fascia__web" style="left:578px">www.vantawallhouse.com</span>
      <span class="fascia__item fascia__phone" style="left:798px">(555) 014-2090</span>
      <span class="fascia__item fascia__brand" style="left:970px">Brelwick Interiors</span>
    </div>

    <div class="window" style="left:97px;width:139px">
      <div class="window__header tagline--purple"><span class="tagline__lead">Don’t Paint Over Potential</span><span class="tagline__main">Wallpaper It</span></div>
      <div class="window__art"><svg viewBox="0 0 100 50" preserveAspectRatio="none" role="img" aria-label="Textured wallpaper roll beside teal marbled wallpaper">
        <rect width="100" height="50" fill="#8a6a4a"/>
        <path d="M44 0 H100 V50 H2 C24 50 56 42 54 32 C52 22 34 12 44 0 Z" fill="var(--swoosh)"/>
        <path d="M50 0 H100 V50 H8 C30 50 62 42 60 32 C58 22 40 12 50 0 Z" fill="#1f6a62"/></svg></div>
    </div>
    <div class="window" style="left:242px;width:140px">
      <div class="window__header tagline--blue"><span class="tagline__lead">Mural of Story?</span><span class="tagline__main">Your Walls Matter</span></div>
      <div class="window__art"><svg viewBox="0 0 100 50" preserveAspectRatio="none" role="img" aria-label="Mural room scene beside dark navy geometric 3D wall panels">
        <rect width="100" height="50" fill="#6f7045"/>
        <path d="M44 0 H100 V50 H2 C24 50 56 42 54 32 C52 22 34 12 44 0 Z" fill="var(--swoosh)"/>
        <path d="M50 0 H100 V50 H8 C30 50 62 42 60 32 C58 22 40 12 50 0 Z" fill="#2c3c52"/></svg></div>
    </div>
    <div class="window" style="left:388px;width:139px">
      <div class="window__header tagline--red"><span class="tagline__lead">Slat Happens</span><span class="tagline__main">We’ll Cover It</span></div>
      <div class="window__art"><svg viewBox="0 0 100 50" preserveAspectRatio="none" role="img" aria-label="Light oak slat panels beside dark walnut slat wall">
        <rect width="100" height="50" fill="#b89870"/>
        <path d="M44 0 H100 V50 H2 C24 50 56 42 54 32 C52 22 34 12 44 0 Z" fill="var(--swoosh)"/>
        <path d="M50 0 H100 V50 H8 C30 50 62 42 60 32 C58 22 40 12 50 0 Z" fill="#6b3322"/></svg></div>
    </div>

    <div class="showroom" role="group" aria-label="Showroom glazing and entrance with torn-paper peel">
      <div class="showroom__glass showroom__glass--left"></div>
      <div class="showroom__glass showroom__glass--right"></div>
      <svg class="showroom__tear" viewBox="0 0 284 67" role="img" aria-label="Torn paper graphic peeling back to reveal the showroom">
        <path d="M0 67 V36 L5 38 L10 34 L16 39 L22 35 L29 40 L35 36 L42 41 L49 37 L56 42 L63 38 L70 43 L77 39 L84 42 L91 40 V67 Z" fill="var(--torn-edge)"/>
        <path d="M0 67 V39 L6 41 L11 37 L17 42 L23 38 L30 43 L36 39 L43 44 L50 40 L57 45 L64 41 L71 46 L78 42 L85 45 L91 43 V67 Z" fill="url(#tear-band)"/>
        <path d="M145 67 V40 L152 42 L159 37 L167 41 L175 36 L183 40 L191 35 L199 39 L207 34 L215 38 L223 33 L231 37 L240 32 L248 36 L257 31 L265 35 L274 30 L284 33 V67 Z" fill="var(--torn-edge)"/>
        <path d="M145 67 V43 L152 45 L159 40 L167 44 L175 39 L183 43 L191 38 L199 42 L207 37 L215 41 L223 36 L231 40 L240 35 L248 39 L257 34 L265 38 L274 33 L284 36 V67 Z" fill="url(#tear-band)"/>
        <path d="M0 0 H22 L17 4 L20 8 L13 11 L15 16 L7 18 L6 24 L0 26 Z" fill="var(--torn-shadow)"/>
        <path d="M0 0 H20 L15 4 L18 8 L11 11 L13 15 L5 17 L4 23 L0 24 Z" fill="url(#tear-flap)"/>
        <path d="M284 0 H258 L263 4 L259 8 L267 11 L264 16 L273 18 L274 24 L284 27 Z" fill="var(--torn-shadow)"/>
        <path d="M284 0 H260 L265 4 L261 8 L269 11 L266 15 L275 17 L276 23 L284 25 Z" fill="url(#tear-flap)"/>
      </svg>
      <div class="entrance"><div class="entrance__frame">
        <div class="entrance__leaf"><div class="entrance__pane"></div><div class="entrance__pane"></div></div>
        <div class="entrance__leaf"><div class="entrance__pane"></div><div class="entrance__pane"></div></div>
      </div></div>
    </div>

    <div class="window" style="left:825px;width:139px">
      <div class="window__header"><span class="window__placeholder tagline--blue">Some Text Here</span></div>
      <div class="window__art"><svg viewBox="0 0 100 50" preserveAspectRatio="none" role="img" aria-label="Bronze wallpaper rolls beside teal and gold scale-pattern mural">
        <rect width="100" height="50" fill="#6a6460"/>
        <path d="M44 0 H100 V50 H2 C24 50 56 42 54 32 C52 22 34 12 44 0 Z" fill="var(--swoosh)"/>
        <path d="M50 0 H100 V50 H8 C30 50 62 42 60 32 C58 22 40 12 50 0 Z" fill="#2a8aa8"/></svg></div>
    </div>
    <div class="window" style="left:972px;width:105px">
      <div class="window__header"><span class="window__placeholder tagline--red">Some Text Here</span></div>
      <div class="window__art"><svg viewBox="0 0 100 50" preserveAspectRatio="none" role="img" aria-label="Stacked wallpaper rolls beside a light crackle-texture room wall">
        <rect width="100" height="50" fill="#7a746a"/>
        <path d="M44 0 H100 V50 H2 C24 50 56 42 54 32 C52 22 34 12 44 0 Z" fill="var(--swoosh)"/>
        <path d="M50 0 H100 V50 H8 C30 50 62 42 60 32 C58 22 40 12 50 0 Z" fill="#c8c6c2"/></svg></div>
    </div>
    <div class="window" style="left:1083px;width:71px">
      <div class="window__header"><span class="window__placeholder tagline--purple">Some Text Here</span></div>
      <div class="window__art"><svg viewBox="0 0 100 50" preserveAspectRatio="none" role="img" aria-label="Landscape mural beside dark green damask wallpaper">
        <rect width="100" height="50" fill="#b8b49c"/>
        <path d="M44 0 H100 V50 H2 C24 50 56 42 54 32 C52 22 34 12 44 0 Z" fill="var(--swoosh)"/>
        <path d="M50 0 H100 V50 H8 C30 50 62 42 60 32 C58 22 40 12 50 0 Z" fill="#3a4a3a"/></svg></div>
    </div>
  </section>

  <!-- Elevation DD -->
  <section class="elevation elevation--dd">
    <span class="elevation__label">-DD-</span>

    <div class="transom" style="left:97px;width:139px;--cols:4"></div>
    <div class="transom" style="left:242px;width:140px;--cols:4"></div>
    <div class="transom" style="left:388px;width:139px;--cols:4"></div>
    <div class="transom" style="left:534px;width:139px;--cols:4"></div>
    <div class="transom" style="left:679px;width:139px;--cols:4"></div>
    <div class="transom" style="left:825px;width:139px;--cols:4"></div>
    <div class="transom" style="left:972px;width:105px;--cols:3"></div>
    <div class="transom" style="left:1083px;width:71px;--cols:2"></div>

    <div class="fascia">
      <span class="fascia__item fascia__category" style="left:70px">WALLPAPER</span>
      <span class="fascia__item fascia__category" style="left:215px">MURALS</span>
      <span class="fascia__item fascia__category" style="left:361px">PANELS</span>
      <span class="fascia__item fascia__web" style="left:578px">www.vantawallhouse.com</span>
      <span class="fascia__item fascia__phone" style="left:798px">(555) 014-2090</span>
      <span class="fascia__item fascia__brand" style="left:970px">Brelwick Interiors</span>
    </div>

    <div class="window" style="left:97px;width:139px">
      <div class="window__header"></div>
      <div class="window__art"><svg viewBox="0 0 100 50" preserveAspectRatio="none" role="img" aria-label="Textured wallpaper roll beside teal marbled wallpaper">
        <rect width="100" height="50" fill="#8a6a4a"/>
        <path d="M44 0 H100 V50 H2 C24 50 56 42 54 32 C52 22 34 12 44 0 Z" fill="var(--swoosh)"/>
        <path d="M50 0 H100 V50 H8 C30 50 62 42 60 32 C58 22 40 12 50 0 Z" fill="#1f6a62"/></svg></div>
      <div class="window__overlay" style="bottom:8px"><span class="tagline__lead">Don’t Paint Over Potential</span><span class="tagline__main">Wallpaper It</span></div>
    </div>
    <div class="window" style="left:242px;width:140px">
      <div class="window__header"></div>
      <div class="window__art"><svg viewBox="0 0 100 50" preserveAspectRatio="none" role="img" aria-label="Mural room scene beside dark navy geometric 3D wall panels">
        <rect width="100" height="50" fill="#6f7045"/>
        <path d="M44 0 H100 V50 H2 C24 50 56 42 54 32 C52 22 34 12 44 0 Z" fill="var(--swoosh)"/>
        <path d="M50 0 H100 V50 H8 C30 50 62 42 60 32 C58 22 40 12 50 0 Z" fill="#2c3c52"/></svg></div>
      <div class="window__overlay"><span class="tagline__lead">Mural of Story?</span><span class="tagline__main">Your Walls Matter</span></div>
    </div>
    <div class="window" style="left:388px;width:139px">
      <div class="window__header"></div>
      <div class="window__art"><svg viewBox="0 0 100 50" preserveAspectRatio="none" role="img" aria-label="Light oak slat panels beside dark walnut slat wall">
        <rect width="100" height="50" fill="#b89870"/>
        <path d="M44 0 H100 V50 H2 C24 50 56 42 54 32 C52 22 34 12 44 0 Z" fill="var(--swoosh)"/>
        <path d="M50 0 H100 V50 H8 C30 50 62 42 60 32 C58 22 40 12 50 0 Z" fill="#6b3322"/></svg></div>
      <div class="window__overlay" style="bottom:6px"><span class="tagline__lead">Slat Happens</span><span class="tagline__main">We’ll Cover It</span></div>
    </div>

    <div class="showroom" role="group" aria-label="Showroom glazing and entrance with torn-paper peel">
      <div class="showroom__glass showroom__glass--left"></div>
      <div class="showroom__glass showroom__glass--right"></div>
      <svg class="showroom__tear" viewBox="0 0 284 67" role="img" aria-label="Torn paper graphic peeling back to reveal the showroom">
        <path d="M0 67 V36 L5 38 L10 34 L16 39 L22 35 L29 40 L35 36 L42 41 L49 37 L56 42 L63 38 L70 43 L77 39 L84 42 L91 40 V67 Z" fill="var(--torn-edge)"/>
        <path d="M0 67 V39 L6 41 L11 37 L17 42 L23 38 L30 43 L36 39 L43 44 L50 40 L57 45 L64 41 L71 46 L78 42 L85 45 L91 43 V67 Z" fill="url(#tear-band)"/>
        <path d="M145 67 V40 L152 42 L159 37 L167 41 L175 36 L183 40 L191 35 L199 39 L207 34 L215 38 L223 33 L231 37 L240 32 L248 36 L257 31 L265 35 L274 30 L284 33 V67 Z" fill="var(--torn-edge)"/>
        <path d="M145 67 V43 L152 45 L159 40 L167 44 L175 39 L183 43 L191 38 L199 42 L207 37 L215 41 L223 36 L231 40 L240 35 L248 39 L257 34 L265 38 L274 33 L284 36 V67 Z" fill="url(#tear-band)"/>
        <path d="M0 0 H22 L17 4 L20 8 L13 11 L15 16 L7 18 L6 24 L0 26 Z" fill="var(--torn-shadow)"/>
        <path d="M0 0 H20 L15 4 L18 8 L11 11 L13 15 L5 17 L4 23 L0 24 Z" fill="url(#tear-flap)"/>
        <path d="M284 0 H258 L263 4 L259 8 L267 11 L264 16 L273 18 L274 24 L284 27 Z" fill="var(--torn-shadow)"/>
        <path d="M284 0 H260 L265 4 L261 8 L269 11 L266 15 L275 17 L276 23 L284 25 Z" fill="url(#tear-flap)"/>
      </svg>
      <div class="entrance"><div class="entrance__frame">
        <div class="entrance__leaf"><div class="entrance__pane"></div><div class="entrance__pane"></div></div>
        <div class="entrance__leaf"><div class="entrance__pane"></div><div class="entrance__pane"></div></div>
      </div></div>
    </div>

    <div class="window" style="left:825px;width:139px">
      <div class="window__header"><span class="window__placeholder window__placeholder--light">Some Text Here</span></div>
      <div class="window__art"><svg viewBox="0 0 100 50" preserveAspectRatio="none" role="img" aria-label="Bronze wallpaper rolls beside teal and gold scale-pattern mural">
        <rect width="100" height="50" fill="#6a6460"/>
        <path d="M44 0 H100 V50 H2 C24 50 56 42 54 32 C52 22 34 12 44 0 Z" fill="var(--swoosh)"/>
        <path d="M50 0 H100 V50 H8 C30 50 62 42 60 32 C58 22 40 12 50 0 Z" fill="#2a8aa8"/></svg></div>
    </div>
    <div class="window" style="left:972px;width:105px">
      <div class="window__header"><span class="window__placeholder window__placeholder--light">Some Text Here</span></div>
      <div class="window__art"><svg viewBox="0 0 100 50" preserveAspectRatio="none" role="img" aria-label="Stacked wallpaper rolls beside a light crackle-texture room wall">
        <rect width="100" height="50" fill="#7a746a"/>
        <path d="M44 0 H100 V50 H2 C24 50 56 42 54 32 C52 22 34 12 44 0 Z" fill="var(--swoosh)"/>
        <path d="M50 0 H100 V50 H8 C30 50 62 42 60 32 C58 22 40 12 50 0 Z" fill="#c8c6c2"/></svg></div>
    </div>
    <div class="window" style="left:1083px;width:71px">
      <div class="window__header"><span class="window__placeholder window__placeholder--light">Some Text Here</span></div>
      <div class="window__art"><svg viewBox="0 0 100 50" preserveAspectRatio="none" role="img" aria-label="Landscape mural beside dark green damask wallpaper">
        <rect width="100" height="50" fill="#b8b49c"/>
        <path d="M44 0 H100 V50 H2 C24 50 56 42 54 32 C52 22 34 12 44 0 Z" fill="var(--swoosh)"/>
        <path d="M50 0 H100 V50 H8 C30 50 62 42 60 32 C58 22 40 12 50 0 Z" fill="#3a4a3a"/></svg></div>
    </div>
  </section>

</main>
</body>
</html>
```